Need a book cover design for a Lumora Book

Book has a long title and sub title so lots of words to fit on the cover.

I can be flexible a bit with the sub title due to the length of it but ideally i can get a design that takes everything.

Here is the title:

Tidal Geology: The Roots of Erosion, Sedimentation, and Canyon Forming

Sub Title/Heading
An Easy Primer on Coastal Cliffs, Dune Drift, River Beds, and Delta Mapping Methods

```html
<!DOCTYPE html>
<html lang="en">
<head>
<meta charset="utf-8">
<title>Tidal Geology — Book Cover</title>
<link href="https://fonts.googleapis.com/css2?family=Noto+Sans:wght@400;700&display=swap" rel="stylesheet">
<style>
  :root {
    --bg-deep: #081216;
    --teal: #4a9aa3;
    --teal-mid: #2c6b74;
    --teal-dark: #14343b;
    --copper: #c0824a;
    --copper-dark: #6e4626;
    --text: #ffffff;
    --panel: rgba(8, 16, 20, 0.5);
  }
  html, body {
    margin: 0;
    padding: 0;
    width: 750px;
    height: 1200px;
    overflow: hidden;
    background: var(--bg-deep);
  }
  .cover {
    position: relative;
    width: 750px;
    height: 1200px;
    overflow: hidden;
    font-family: "Noto Sans", sans-serif;
    color: var(--text);
  }
  .cover-art {
    position: absolute;
    inset: 0;
    background:
      radial-gradient(ellipse 38% 9% at 42% 640px, rgba(192,130,74,0.75), transparent 75%),
      radial-gradient(ellipse 30% 6% at 70% 560px, rgba(192,130,74,0.55), transparent 75%),
      radial-gradient(ellipse 40% 7% at 38% 150px, rgba(192,130,74,0.5), transparent 75%),
      radial-gradient(ellipse 30% 12% at 92% 1080px, rgba(192,130,74,0.45), transparent 75%),
      radial-gradient(ellipse 42% 14% at 40% 700px, rgba(140,170,175,0.45), transparent 75%),
      radial-gradient(ellipse 55% 16% at 50% 110px, rgba(74,154,163,0.6), transparent 75%),
      radial-gradient(ellipse 30% 20% at 8% 380px, rgba(74,154,163,0.55), transparent 75%),
      radial-gradient(ellipse 25% 25% at 90% 400px, rgba(74,154,163,0.45), transparent 75%),
      radial-gradient(ellipse 70% 18% at 40% 1130px, rgba(74,154,163,0.7), transparent 75%),
      radial-gradient(ellipse 30% 18% at 10% 900px, rgba(44,107,116,0.7), transparent 75%),
      linear-gradient(165deg, var(--teal-dark) 0%, var(--bg-deep) 30%, var(--teal-dark) 50%, var(--bg-deep) 70%, var(--teal-mid) 100%);
  }
  .title-panel {
    position: absolute;
    left: 68px;
    top: 261px;
    width: 614px;
    height: 210px;
    box-sizing: border-box;
    padding-top: 16px;
    background: var(--panel);
    text-align: center;
  }
  .title-main {
    margin: 0;
    font-size: 66px;
    font-weight: 700;
    line-height: 76px;
  }
  .title-sub {
    margin: 0;
    font-size: 32px;
    font-weight: 400;
    line-height: 50px;
  }
  .subtitle-panel {
    position: absolute;
    left: 90px;
    top: 803px;
    width: 570px;
    height: 205px;
    box-sizing: border-box;
    padding-top: 4px;
    background: var(--panel);
    text-align: center;
  }
  .subtitle {
    margin: 0;
    font-size: 32px;
    font-weight: 400;
    line-height: 50px;
  }
</style>
</head>
<body>
  <main class="cover">
    <div class="cover-art" role="img" aria-label="Abstract swirling ribbons of teal and copper strands on a dark background"></div>

    <header class="title-panel">
      <h1 class="title-main">Tidal Geology:</h1>
      <p class="title-sub">The Roots of Erosion, Sedimentation,<br>and Canyon Forming</p>
    </header>

    <section class="subtitle-panel">
      <p class="subtitle">An Easy Primer<br>on Coastal Cliffs, Dune Drift,<br>River Beds, and Delta<br>Mapping Methods</p>
    </section>
  </main>
</body>
</html>
```